Rusty Lantern Ale Room & Sports Kitchen Menu

This is my dine in menu for my sports bar. I would like it to be playful and fun. The colors of my logo are also the colors of my bar. You can look at facebook or rustylanternaleroom.com to see pictures. My current menu is a trifold and I would like to move away from that design. I like a the menu to flow, but am very open to new concepts. I feel like my current one is too boring and not professional enough as well as not catchy. I like a colored page, with colored lettering not necessarily black or white text. I currently use the colors of my log on my menu but like the idea of something that is not boring.

Target Market(s)

customers coming into my bar

Industry/Entity Type

Sports Bar

Requirements
Must have
• LOGO, Specials,
Nice to have
• pictures of food
Should not have
• open to all designs

```html
<!DOCTYPE html>
<html lang="en">
<head>
<meta charset="utf-8">
<title>Rusty Lantern Ale Room &amp; Sports Kitchen — Menu</title>
<link href="https://fonts.googleapis.com/css2?family=Alfa+Slab+One&family=Kalam:wght@400;700&display=swap" rel="stylesheet">
<style>
:root{
  --night:#1f1f1f;
  --paper:#efeeeb;
  --ink:#1c1c1c;
  --orange:#e8892c;
  --orange-deep:#e07f22;
  --blue:#27a3dc;
  --green:#63b85a;
  --white:#ffffff;
}
*{margin:0;padding:0;box-sizing:border-box}
html,body{width:1200px;height:927px;overflow:hidden;background:var(--night)}
.menu{position:relative;width:1200px;height:927px;background:var(--night);overflow:hidden}
.paper{position:absolute;left:0;top:0;width:1200px;height:927px}
.block{position:absolute;text-align:center;color:var(--ink);font-family:"Kalam",cursive}
.band{position:absolute;display:flex;flex-direction:column;align-items:center;justify-content:center;color:var(--white)}
.band h2{font-family:"Kalam",cursive;font-weight:700;font-size:28px;letter-spacing:1px;line-height:1}
.band-burgers{left:53px;top:61px;width:505px;height:40px;background:var(--orange)}
.ribbon{left:94px;top:121px;width:424px;height:42px;background:var(--orange);font-family:"Kalam",cursive;font-weight:700;font-size:9.5px;line-height:1.2;text-align:center;padding:0 10px}
.band-salads{left:53px;top:429px;width:505px;height:42px;background:var(--blue)}
.band-salads p{font-family:"Kalam",cursive;font-size:9px;font-weight:700;margin-top:0;line-height:1.1}
.item-title{font-family:"Alfa Slab One",serif;font-size:9.5px;font-weight:400;letter-spacing:.3px;text-transform:uppercase;line-height:1.2}
.item-desc{font-size:9.5px;font-style:italic;font-weight:700;line-height:1.3;margin-top:3px}
.prices{display:flex;justify-content:center;gap:40px;font-size:9.5px;font-weight:700;margin-top:3px}
.specials{position:absolute;left:53px;top:676px;width:492px;height:202px;background:linear-gradient(180deg,#6fc062 0%,#5fb257 55%,#8a9a5e 100%);color:var(--white);font-family:"Kalam",cursive}
.specials h3{position:absolute;left:0;top:8px;width:100%;text-align:center;font-family:"Kalam",cursive;font-weight:700;font-size:20px;letter-spacing:1.5px;line-height:1.1}
.day{position:absolute;text-align:center;font-size:9px;line-height:1.2;text-transform:uppercase}
.day b{display:block;font-weight:700;font-size:11px;letter-spacing:.5px}
.note{position:absolute;font-size:8.5px;line-height:1.2}
.fine{position:absolute;left:8px;top:176px;width:476px;font-size:7.5px;line-height:1.15}
.brand{position:absolute;left:760px;top:478px;width:400px;text-align:center;color:var(--white);font-family:"Alfa Slab One",serif;font-size:24px;line-height:1.2;letter-spacing:1px}
</style>
</head>
<body>
<main class="menu">
  <svg class="paper" viewBox="0 0 1200 927" aria-hidden="true">
    <polygon fill="var(--paper)" points="33,0 700,0 690,40 702,90 688,150 700,210 686,270 698,330 684,400 697,470 685,540 699,610 686,690 698,760 690,830 700,880 688,909 33,909"/>
    <polygon fill="var(--orange-deep)" points="720,0 1200,0 1200,927 705,927 716,880 703,830 712,760 700,690 714,610 701,540 712,470 698,400 713,330 702,270 716,210 703,150 718,90 706,40"/>
  </svg>

  <header class="band band-burgers"><h2>Burgers</h2></header>
  <div class="band ribbon">Choice Of American, Cheddar, Swiss, Pepper Jack, Provolone<br>Brioche Bun Or Sub Roll Bun, Come With A Side Of Fries Or Chips. (Lettuce/Tomatoes/Pickles On Request Only)</div>

  <section class="block" style="left:55px;top:190px;width:215px">
    <h4 class="item-title">Ground Bacon Burger w/Cheese</h4>
    <p class="item-desc">One Third Pound Burger Is 70% Ground Bacon &amp; 30% Beef. It's Covered With Your Choice Of Cheese And 3 Strips Of Bacon. – 10.95</p>
  </section>
  <section class="block" style="left:55px;top:256px;width:215px">
    <h4 class="item-title">Cheeseburger</h4>
    <p class="item-desc">Quarter Pound Burger Topped With Your Choice Of Cheese.</p>
    <p class="prices"><span>Single – 7.95</span><span>Double – 9.95</span></p>
  </section>
  <section class="block" style="left:325px;top:190px;width:240px">
    <h4 class="item-title">Italian Cheeseburger</h4>
    <p class="item-desc">Quarter Pound Burger Topped With Capicola &amp; Your Choice Of Cheese. – 11.95</p>
  </section>
  <section class="block" style="left:325px;top:250px;width:240px">
    <h4 class="item-title">Pastrami Cheeseburger</h4>
    <p class="item-desc">Quarter Pound Burger Topped With Pastrami &amp; Your Choice Of Cheese. – 11.95</p>
  </section>
  <section class="block" style="left:165px;top:326px;width:330px">
    <h4 class="item-title">Bad A$$ Philly Burger</h4>
    <p class="item-desc">Two ¼ Lb Patties Topped With American Cheese. On Top Of The Patties You Will Find Philly Meat, Grilled Onions, &amp; More American Cheese. You Get The Best Of Both Worlds, A Burger And A Philly Put Together On A Sub Roll, Get The Napkins Ready, You're In For A Treat!!!! – 15.95</p>
  </section>

  <header class="band band-salads"><h2>Salads</h2><p>Ranch, Greek Feta, Blue Cheese, Italian, 1000 Island</p></header>

  <section class="block" style="left:55px;top:506px;width:215px">
    <p class="item-desc" style="margin-top:0">Ranch, Greek Feta, Blue Cheese, Italian, 1000 Island</p>
  </section>
  <section class="block" style="left:55px;top:532px;width:215px">
    <h4 class="item-title">Chicken Tender Salad</h4>
    <p class="item-desc">Sliced Chicken Tenders Served Over Sliced Lettuce, Topped With Tomatoes, Shredded Cheddar, Cucumbers, Red Onions, &amp; Croutons. – 10.95</p>
  </section>
  <section class="block" style="left:55px;top:610px;width:215px">
    <h4 class="item-title">Grilled Chicken Salad</h4>
    <p class="item-desc">Seasoned And Grilled Chicken Breast Served Over Sliced Lettuce, Topped With Tomatoes, Shredded Cheddar, Cucumbers, Red</p>
  </section>
  <section class="block" style="left:325px;top:508px;width:240px">
    <h4 class="item-title">Chef Salad</h4>
    <p class="item-desc">Ham And Turkey Served Over Sliced Lettuce, Topped With Tomatoes, Shredded Cheddar Cheese, Cucumbers, Red Onions, Hardboiled Egg, &amp; Croutons. – 10.95</p>
  </section>
  <section class="block" style="left:325px;top:583px;width:240px">
    <h4 class="item-title">Gyro Salad</h4>
    <p class="item-desc">Gyro Meat Covered In Tzatziki Sauce Served Over Sliced Lettuce, Topped With Tomatoes, Shredded Cheddar, Cucumbers, Red Onions, &amp; Croutons. – 10.95</p>
  </section>

  <section class="specials" role="img" aria-label="Daily specials panel over a photo of bar food plates">
    <h3>Daily Specials</h3>
    <p class="day" style="left:0;top:38px;width:250px"><b>Sunday</b>Happy Hour All Day</p>
    <p class="day" style="left:0;top:74px;width:250px"><b>Monday</b>$2 Domestic Pints, $2.50 BM &amp; Dos Rios All Day</p>
    <p class="day" style="left:0;top:110px;width:250px"><b>Tuesday</b>$3.50 Domestic Talls, $4 BM &amp; Dos Rios All Day</p>
    <p class="day" style="left:0;top:144px;width:250px"><b>Wednesday</b>$4 Wells &amp; .40¢ Off Wings All Day</p>
    <p class="day" style="left:250px;top:38px;width:242px"><b>Thursday</b>Happy Hour All Day</p>
    <p class="day" style="left:250px;top:74px;width:242px"><b>Friday</b>$4 Cinnamon Shots &amp; $8 Phillies w/Fries or Chips</p>
    <p class="day" style="left:250px;top:110px;width:242px"><b>Saturday</b>$3 Domestic Tall Drafts All Day</p>
    <p class="note" style="left:262px;top:148px;width:226px">*Specials not valid for special events or fight nights</p>
    <p class="fine">Happy hour including - $4 well drinks, tall bm/dos rios, &amp; food menu, $2.50 pints &amp; domestic bottles, $3.50 domestic tall drafts monday, tuesday, wednesday, friday 11-7pm, 7pm-cl Sunday &amp; thursday all day happy hour</p>
  </section>

  <h1 class="brand">RUSTY LANTERN<br>ALE ROOM &amp; SPORTS KITCHEN</h1>
</main>
</body>
</html>
```